Keelbrook Vault Holdings Needs A Website

We are looking for a website for a new company. 4 Pages

Needs to be responsive and mobile friendly for all browsers and coded for both Android & IOS. SEO is also important.

Website Brief – Keelbrook Vault Holdings
Domain: www.keelbrookvault.net
Email: info@keelbrookvault.net
Phone: to be inserted later
Address: 40837 52 Ave, Edmonton, AB T6K 3R8
Platform: WordPress (recommended for flexibility, SEO tools, and ease of editing)
Requirements:
• Responsive & mobile-friendly (Android & iOS)
• Cross-browser compatibility
• Fast page load speed
• SEO optimized for storage development, management, and investment keywords
• Easy in-house editing after launch
• Professional, modern, trust-driven design reflecting expertise, reliability, and innovation
________________________________________
Pages
1. HOME
Purpose: Quickly communicate who Keelbrook Vault Holdings is and why they’re the best choice for designing, building, leasing, and managing self storage facilities.
Content Highlights:
• Hero Section: Large, bold image of a modern self storage facility with headline:
"From Concept to Capacity – Your Self Storage Experts"
• Subheadline: “Keelbrook Vault Holdings delivers turnkey design, construction, leasing, and management services for profitable self storage operations.”
• Quick Service Icons:
o Facility Design & Development
o Construction & Build Management
o Lease-Up & Marketing
o Ongoing Facility Management
• Call to Action Button: “LEARN MORE” → links to ABOUT US page.
• Featured Project Highlights: Showcase a few completed or current projects with photos and stats.
• Contact Banner: “Ready to build your next self storage project? Let’s talk.” → CONTACT page.
2. ABOUT US
Purpose: Build credibility, showcase experience, and explain the value proposition.
Content Highlights:
• Who We Are: Overview of Keelbrook Vault Holdings’ history, mission, and team expertise.
• Our Approach: End-to-end process from site selection to occupancy.
• Why Choose Us:
o Industry expertise in self storage
o Proven track record in lease-up success
o Strong vendor and contractor network
3. SERVICES
Purpose: Detail all service offerings with clarity and authority.
Sections:
• Design & Development: Market analysis, site planning, and architectural design.
• Construction Management: Overseeing timelines, budgets, and quality control.
• Lease-Up Strategy: Marketing, promotions, and occupancy acceleration.
• Ongoing Facility Management: Staffing, maintenance, revenue optimization.

4. CONTACT
Purpose: Provide simple, direct ways to connect.
Content Highlights:
• Contact Form (Name, Email, Phone, Message)
• Direct Email: info@keelbrookvault.net
• Phone (if applicable)
• Google Map embed (if there’s a head office location)
• CTA: “Let’s Build Your Storage Success Story.”
Design & Technical Notes
• Visual Style: Clean, modern, bold typography, professional color palette (to be based on branding), strong imagery of self storage facilities.
• Performance: Image compression, caching, responsive scaling.
• SEO Targets: “Self storage facility developer,” “self storage construction,” “self storage management company,” “lease-up services for self storage.”

WordPress or Joomla – must be desktop and mobile friendly with fast page load speed. Need the ability to edit ourselves.

Use pantone colours - #033c5a – dark blue
#2baadf – light blue

```html
<!DOCTYPE html>
<html lang="en">
<head>
<meta charset="UTF-8">
<title>Contact – Keelbrook Vault Holdings</title>
<link href="https://fonts.googleapis.com/css2?family=Poppins:wght@300;400;500;600;700&display=swap" rel="stylesheet">
<style>
:root{
  --navy:#033c5a;
  --sky:#2baadf;
  --ink:#1f2a33;
  --muted:#5b6670;
  --line:#d9dfe4;
  --panel:#f4f6f8;
  --white:#ffffff;
}
*{box-sizing:border-box;margin:0;padding:0}
html,body{width:1200px;height:3556px;overflow:hidden}
body{font-family:"Poppins",sans-serif;color:var(--ink);background:var(--white);position:relative}
.abs{position:absolute}

/* header */
.site-header{left:0;top:0;width:1200px;height:140px;background:var(--white);display:flex;align-items:center;padding:0 60px 0 48px;z-index:3;border-radius:0 0 40px 40px}
.brand{display:flex;align-items:center;gap:14px}
.brand-square{width:40px;height:40px;background:var(--navy)}
.brand-name{color:var(--navy);font-weight:600;font-size:26px;line-height:1.1;width:260px}
.main-nav{margin-left:auto;display:flex;align-items:center;gap:34px;font-size:16px;font-weight:500}
.main-nav a{color:var(--ink);text-decoration:none}
.main-nav a.active{color:var(--sky)}
.btn{display:inline-flex;align-items:center;justify-content:center;border-radius:40px;font-weight:600;text-transform:uppercase;text-decoration:none;letter-spacing:.5px}
.btn-header{background:var(--sky);color:var(--white);width:176px;height:58px;font-size:15px;margin-left:26px}

/* hero */
.hero{left:0;top:0;width:1200px;height:1000px;background:linear-gradient(180deg,#3a7fae 0%,#5fa9d6 40%,#2d6f9e 75%,#1c5a85 100%)}
.hero-shape{left:0;top:760px;width:1200px;height:260px}
.hero-title{left:0;top:545px;width:1200px;text-align:center;color:var(--white);font-weight:600;font-size:50px;line-height:64px}
.hero-sub{left:300px;top:686px;width:600px;text-align:center;color:var(--white);font-size:16px;line-height:28px}
.btn-hero{left:500px;top:775px;width:200px;height:60px;background:var(--white);color:var(--sky);font-size:16px}

/* contact intro */
.section-title{left:0;top:1105px;width:1200px;text-align:center;font-size:46px;font-weight:600;color:var(--navy)}
.section-title span{color:var(--sky)}
.title-rule{left:550px;top:1182px;width:100px;height:4px;background:var(--navy)}
.intro-text{left:170px;top:1220px;width:860px;text-align:center;font-size:17px;line-height:30px;color:var(--muted)}

/* contact panel */
.contact-panel{left:120px;top:1378px;width:932px;height:810px;background:var(--panel)}
.panel-photo{left:0;top:0;width:410px;height:810px;background:linear-gradient(180deg,#0d4b73 0%,#1a6794 45%,#0b3f62 100%)}
.info-item{left:60px;display:flex;align-items:center;gap:22px;color:var(--white)}
.info-icon{width:66px;height:66px;border-radius:50%;background:var(--white);display:flex;align-items:center;justify-content:center;flex:none}
.info-label{font-size:19px;font-weight:500;text-transform:uppercase;letter-spacing:.5px}
.info-value{font-size:13px;opacity:.9}
.form-area{left:460px;top:0;width:420px}
.form-title{position:absolute;left:0;top:60px;width:440px;text-align:center;font-size:34px;font-weight:600;color:var(--ink)}
.field-label{position:absolute;left:0;font-size:12px;font-weight:600;text-transform:uppercase;color:var(--ink)}
.field{position:absolute;height:46px;border:1px solid var(--line);background:var(--white);font-size:13px;color:#9aa3ab;padding:0 14px;display:flex;align-items:center}
.field.tall{height:180px;align-items:flex-start;padding-top:12px}
.btn-send{position:absolute;left:156px;top:526px;width:180px;height:54px;background:var(--sky);color:var(--white);font-size:15px;border-radius:4px}

/* map */
.map{left:0;top:2300px;width:1200px;height:580px;background:linear-gradient(135deg,#c9d9c0 0%,#e3e7dc 40%,#d6dfd0 70%,#bfd2b8 100%)}
.map-pin{left:762px;top:2535px}
.btn-story{left:400px;top:2934px;width:400px;height:62px;background:var(--sky);color:var(--white);font-size:15px;border-radius:6px}

/* footer */
.footer-shape{left:0;top:3030px;width:1200px;height:170px}
.footer-brand{left:150px;top:3240px}
.footer-brand .brand-name{font-size:24px;width:230px}
.social{left:224px;top:3320px;display:flex;gap:10px}
.social span{width:28px;height:28px;border-radius:50%;background:var(--sky)}
.footer-col{top:3182px}
.footer-col h3{font-size:30px;font-weight:500;color:var(--navy);margin-bottom:24px}
.footer-links li{list-style:none;font-size:16px;color:var(--ink);margin-bottom:14px;display:flex;align-items:center;gap:14px}
.footer-links li::before{content:"";width:8px;height:8px;border-radius:50%;background:var(--sky)}
.footer-contact li{list-style:none;display:flex;align-items:center;gap:16px;font-size:15px;margin-bottom:18px;line-height:22px}
.footer-contact .dot{width:42px;height:42px;border-radius:50%;background:var(--navy);display:flex;align-items:center;justify-content:center;flex:none}
.footer-rule{left:120px;top:3480px;width:960px;height:1px;background:var(--line)}
.copyright{left:0;top:3506px;width:1200px;text-align:center;font-size:14px;color:var(--ink)}
</style>
</head>
<body>

<div class="hero abs" role="img" aria-label="Photo of a modern self storage warehouse interior with loading doors and a truck"></div>
<svg class="hero-shape abs" viewBox="0 0 1200 260" aria-hidden="true">
  <polygon points="0,40 600,200 1200,40 1200,260 0,260" fill="#ffffff"/>
  <polyline points="0,30 600,190 1200,30" fill="none" stroke="#033c5a" stroke-width="26"/>
</svg>

<header class="site-header abs">
  <div class="brand">
    <span class="brand-square"></span>
    <span class="brand-name">Keelbrook Vault Holdings</span>
  </div>
  <nav class="main-nav">
    <a class="active" href="#">Home</a>
    <a href="#">About Us</a>
    <a href="#">Services</a>
    <a href="#">Featured Project</a>
    <a class="btn btn-header" href="#">Contact Us</a>
  </nav>
</header>

<h1 class="hero-title abs">From Concept to Capacity – Your<br>Self Storage Experts</h1>
<p class="hero-sub abs">Keelbrook Vault Holdings delivers turnkey design, construction, leasing, and management services for profitable self storage operations.</p>
<a class="btn btn-hero abs" href="#">Contact Now</a>

<h2 class="section-title abs">Contact <span>Us</span></h2>
<div class="title-rule abs"></div>
<p class="intro-text abs">Lorem ipsum dolor sit amet, consectetur adipiscing elit, sed do eiusmod tempor incididunt ut labore et dolore magna aliqua. Quis ipsum suspendisse ultrices gravida. Risus commodo viverra maecenas accumsan lacus vel facilisis.</p>

<section class="contact-panel abs">
  <div class="panel-photo abs" role="img" aria-label="Photo of a storage warehouse interior tinted dark blue"></div>

  <div class="info-item abs" style="top:208px">
    <span class="info-icon"><svg width="28" height="28" viewBox="0 0 24 24"><path d="M12 2a7 7 0 0 0-7 7c0 5 7 13 7 13s7-8 7-13a7 7 0 0 0-7-7zm0 9.5A2.5 2.5 0 1 1 12 6.5a2.5 2.5 0 0 1 0 5z" fill="#033c5a"/></svg></span>
    <div><div class="info-label">Location</div><div class="info-value">40837 52 Ave, Edmonton</div></div>
  </div>
  <div class="info-item abs" style="top:370px">
    <span class="info-icon"><svg width="28" height="28" viewBox="0 0 24 24"><path d="M6.6 10.8a15 15 0 0 0 6.6 6.6l2.2-2.2a1 1 0 0 1 1-.25 11.4 11.4 0 0 0 3.6.57 1 1 0 0 1 1 1V20a1 1 0 0 1-1 1A17 17 0 0 1 3 4a1 1 0 0 1 1-1h3.5a1 1 0 0 1 1 1c0 1.25.2 2.45.57 3.57a1 1 0 0 1-.25 1z" fill="#033c5a"/></svg></span>
    <div><div class="info-label">Call Us</div><div class="info-value">987 654 3210</div></div>
  </div>
  <div class="info-item abs" style="top:536px">
    <span class="info-icon"><svg width="28" height="28" viewBox="0 0 24 24"><path d="M3 5h18v14H3z" fill="#033c5a"/><path d="M3 5l9 7 9-7" fill="none" stroke="#fff" stroke-width="1.6"/></svg></span>
    <div><div class="info-label">Email Us</div><div class="info-value">info@keelbrookvault.net</div></div>
  </div>

  <form class="form-area abs">
    <h3 class="form-title">Send Us A Message</h3>
    <label class="field-label" style="top:190px">Tell us your name *</label>
    <div class="field" style="left:0;top:212px;width:200px">First Name</div>
    <div class="field" style="left:220px;top:212px;width:200px">Last Name</div>
    <label class="field-label" style="top:280px">Enter your email *</label>
    <div class="field" style="left:0;top:300px;width:420px">Email</div>
    <label class="field-label" style="top:366px">Enter phone number</label>
    <div class="field" style="left:0;top:386px;width:420px">Phone</div>
    <label class="field-label" style="top:448px">Message *</label>
    <div class="field tall" style="left:0;top:468px;width:420px;height:40px"></div>
    <a class="btn btn-send" href="#">Send Message</a>
  </form>
</section>

<div class="map abs" role="img" aria-label="Map showing the head office location in Edmonton"></div>
<svg class="map-pin abs" width="30" height="42" viewBox="0 0 24 34" aria-hidden="true"><path d="M12 0a12 12 0 0 0-12 12c0 9 12 22 12 22s12-13 12-22A12 12 0 0 0 12 0z" fill="#d93025"/><circle cx="12" cy="12" r="4" fill="#7a1410"/></svg>

<a class="btn btn-story abs" href="#">Let's Build Your Storage Success Story</a>

<svg class="footer-shape abs" viewBox="0 0 1200 170" aria-hidden="true">
  <polyline points="0,160 600,12 1200,160" fill="none" stroke="#033c5a" stroke-width="20"/>
</svg>

<footer>
  <div class="footer-brand brand abs">
    <span class="brand-square"></span>
    <span class="brand-name">Keelbrook Vault Holdings</span>
  </div>
  <div class="social abs"><span></span><span></span><span></span></div>

  <div class="footer-col abs" style="left:520px">
    <h3>Links</h3>
    <ul class="footer-links">
      <li>About Us</li>
      <li>Services</li>
      <li>Featured Project</li>
      <li>Contact Us</li>
    </ul>
  </div>

  <div class="footer-col abs" style="left:798px">
    <h3>Contact Us</h3>
    <ul class="footer-contact">
      <li><span class="dot"><svg width="20" height="20" viewBox="0 0 24 24"><path d="M12 2a7 7 0 0 0-7 7c0 5 7 13 7 13s7-8 7-13a7 7 0 0 0-7-7zm0 9.5A2.5 2.5 0 1 1 12 6.5a2.5 2.5 0 0 1 0 5z" fill="#fff"/></svg></span>40837 52 Ave, Edmonton,<br>AB T6K 3R8</li>
      <li><span class="dot"><svg width="20" height="20" viewBox="0 0 24 24"><path d="M6.6 10.8a15 15 0 0 0 6.6 6.6l2.2-2.2a1 1 0 0 1 1-.25 11.4 11.4 0 0 0 3.6.57 1 1 0 0 1 1 1V20a1 1 0 0 1-1 1A17 17 0 0 1 3 4a1 1 0 0 1 1-1h3.5a1 1 0 0 1 1 1c0 1.25.2 2.45.57 3.57a1 1 0 0 1-.25 1z" fill="#fff"/></svg></span>987 654 3210</li>
      <li><span class="dot"><svg width="20" height="20" viewBox="0 0 24 24"><path d="M3 5h18v14H3z" fill="#fff"/><path d="M3 5l9 7 9-7" fill="none" stroke="#033c5a" stroke-width="1.6"/></svg></span>info@keelbrookvault.net</li>
    </ul>
  </div>

  <div class="footer-rule abs"></div>
  <p class="copyright abs">Copyright © 2025 All Rights Reserved By Keelbrook Vault Holdings</p>
</footer>

</body>
</html>
```